Community-based social network needs a new landing page

We need a landing page for a local social network in Singapore called "NestLinker.sg". It is a website that help neighbours to connect with each other for mutual benefits such as providing professional/non-professional services, sharing items, and neighbourly help, etc.

There is an existing website but we want to completely revamp it. It is most important that the new landing page communicates that the neighbourhood has skills and services for people to discover.

The final design of the landing page should be modern, and communicates a sense of community and vibrancy. As a matter of priority, more real estate should be accorded to the neighbours providing services elements.

We have drafted 2 reference sites that communicates the key ideas/user propositions for your easy reference:
http://tavrilo82.pageforge.example/nestlinker
http://tavrilo82.pageforge.example/nestlinker2

As long as the key ideas/user propositions are kept to, we are open to any design proposals. I.e. you do not have to follow the design layout of the reference sites

Target Market(s)

Our target market is primarily the Singapore community, includes all genders, education levels and occupations, aged between 17-45 years old.

In the file uploaded, you will find pictures of Singapore neighbourhoods and people of local ethnicities. Please use them, but you may arrange and add further filters to better enhance them

Industry/Entity Type

Real Estate

Requirements
Nice to have
• Landing page could be similar to that of www.gatherkite.example, not just at the top, but also the way the other categories are presented at the bottom.

```html
<!DOCTYPE html>
<html lang="en">
<head>
<meta charset="utf-8">
<title>NestLinker.sg</title>
<link href="https://fonts.googleapis.com/css2?family=Questrial&family=Open+Sans:wght@400;600&display=swap" rel="stylesheet">
<style>
:root{
  --dark:#4a4a4a;
  --white:#ffffff;
  --red:#d5143a;
  --navy:#1f3c6e;
  --green:#6b9b3a;
  --teal:#3a9ec0;
  --gray:#6d6d6d;
  --line:#e3e3e3;
  --sky:#d3e6f8;
  --yellow:#f7c200;
  --blue-btn:#3e5f9e;
  --lime:#8cc63f;
}
*{box-sizing:border-box;margin:0;padding:0}
html,body{width:1186px;height:1200px;overflow:hidden}
body{font-family:"Open Sans",Arial,sans-serif;background:var(--white);position:relative}
.abs{position:absolute}
.topbar{left:0;top:0;width:1186px;height:99px;background:var(--dark)}
.brand{left:124px;top:28px;display:flex;align-items:center;gap:10px;font-family:"Questrial",sans-serif;font-size:30px;color:var(--white)}
.brand-mark{width:22px;height:22px;background:var(--yellow)}
.login-label{color:var(--white);font-size:13px}
.login-field{height:20px;background:#f1f1f1;border:1px solid #bbb;border-radius:3px;box-shadow:inset 0 1px 3px rgba(0,0,0,.25)}
.login-small{color:#e0e0e0;font-size:11px}
.remember-box{width:9px;height:9px;background:#eee;border:1px solid #999}
.btn-login{left:892px;top:37px;width:60px;height:18px;background:var(--yellow);border-radius:2px;color:#5a4500;font-size:12px;font-weight:600;text-align:center;line-height:18px}
.or{left:967px;top:40px;color:#eee;font-size:12px;font-family:Georgia,serif}
.btn-connect{left:997px;top:35px;width:72px;height:22px;background:var(--blue-btn);border:1px solid #2c477a;border-radius:3px;color:var(--white);font-size:11px;font-weight:600;text-align:center;line-height:20px}
.hero{left:0;top:99px;width:1186px;height:479px;background:linear-gradient(180deg,#dfe6ee 0%,#c9d3dc 35%,#9aa8b4 60%,#6d7780 85%,#4e4a44 100%)}
.portrait{width:126px;height:118px;border:5px solid var(--white);background:linear-gradient(160deg,#c9a88e,#8f6a55);box-shadow:0 1px 4px rgba(0,0,0,.3)}
.portrait.second{background:linear-gradient(160deg,#e3d6c8,#7b8794)}
.callout{background:var(--white);padding:5px 10px;font-family:"Questrial",sans-serif;font-size:17.5px;line-height:21px;color:#111}
.pin{width:20px;height:26px}
.feature-title{font-family:"Questrial",sans-serif;font-size:22px;color:var(--red);line-height:23px}
.feature-rule{height:1px;background:var(--line);width:283px}
.feature-text{font-size:12.5px;color:var(--gray);line-height:20px;width:285px}
.go{font-size:12px;color:#333;font-style:italic;text-decoration:underline}
.col-divider{width:1px;height:198px;top:578px;background:linear-gradient(180deg,#fff,#e6e6e6,#fff)}
.lower{left:0;top:776px;width:1186px;height:362px;background:linear-gradient(180deg,#d9eaf9,#cde2f6)}
.section-title{font-family:"Questrial",sans-serif;font-size:22px;top:810px}
.listings{left:127px;top:848px;width:294px;height:241px;background:var(--white);border:2px solid #d0d6dc;box-shadow:0 0 3px rgba(0,0,0,.15)}
.listing-thumb{width:53px;height:53px;border-radius:4px;background:linear-gradient(160deg,#a58a76,#4f4a48)}
.listing-thumb.light{background:linear-gradient(160deg,#e8c9a0,#b98e62)}
.listing-title{font-size:13px;color:#111}
.listing-rule{width:193px;border-top:1px dotted #bbb}
.listing-text{font-size:11.5px;color:#555;line-height:14.5px;width:195px}
.listing-meta{font-size:11px;color:#aaa}
.scroll-track{left:281px;top:20px;width:4px;height:196px;background:#e5e8eb;border-radius:2px}
.scroll-thumb{left:281px;top:52px;width:4px;height:28px;background:#7d9cc4;border-radius:2px}
.member{width:66px;height:66px;border:1px solid #c2ccd6;background:linear-gradient(160deg,#bfa38d,#6c5a50)}
.promo{left:446px;top:1017px;font-family:"Questrial",sans-serif;font-size:19px;line-height:24px;color:var(--teal);font-weight:600}
.show-all{left:447px;top:1077px;font-size:11px;color:#333;text-decoration:underline}
.signup{left:763px;top:845px;width:298px;height:250px;border:3px solid #b8d2ec;background:#f4f8fc}
.signup-title{left:22px;top:14px;font-size:14px;letter-spacing:1.5px;color:#2d3f55}
.signup-rule{left:12px;top:41px;width:270px;height:1px;background:#9fb4c8}
.signup-field{left:20px;width:249px;height:28px;background:var(--white);border:1px solid #c8ccd0;padding-left:17px;font-size:13px;letter-spacing:1px;color:#444;line-height:26px}
.btn-next{left:20px;top:140px;width:76px;height:29px;background:linear-gradient(180deg,#e9e9e9,#c9c9c9);border:1px solid #aaa;border-radius:2px;font-size:14px;letter-spacing:1px;color:#555;text-align:center;line-height:27px}
.agree{left:160px;top:146px;font-size:11px;color:#444}
.agree-box{left:204px;top:147px;width:12px;height:12px;border:1px solid #3a6fb0;background:var(--white)}
.signup-link{left:20px;font-size:9.5px;letter-spacing:.8px;color:#555}
.footer{left:0;top:1138px;width:1186px;height:62px;background:var(--dark)}
.footer-text{top:1163px;color:var(--white);font-size:12.5px}
.share-btn{top:1162px;height:17px;background:#eef2f7;border:1px solid #b8c2ce;border-radius:2px;font-size:9.5px;color:#3b5a8a;text-align:center;line-height:15px;font-weight:600}
</style>
</head>
<body>

<header class="abs topbar"></header>
<div class="abs brand"><span class="brand-mark"></span>NestLinker.sg</div>

<div class="abs login-label" style="left:510px;top:17px">Username or Email</div>
<div class="abs login-field" style="left:507px;top:36px;width:183px"></div>
<div class="abs remember-box" style="left:511px;top:61px"></div>
<div class="abs login-small" style="left:527px;top:58px">Remember me logged in</div>

<div class="abs login-label" style="left:702px;top:17px">Password</div>
<div class="abs login-field" style="left:699px;top:36px;width:181px"></div>
<div class="abs login-small" style="left:701px;top:58px">Forgotten your password?</div>

<div class="abs btn-login">Login</div>
<div class="abs or">OR</div>
<div class="abs btn-connect">Connect</div>

<section class="abs hero" role="img" aria-label="Softly blurred photo of the Singapore city skyline with tall towers under a bright sky"></section>

<div class="abs portrait" style="left:193px;top:194px" role="img" aria-label="Photo of Aisha smiling while holding a red guitar"></div>
<div class="abs callout" style="left:318px;top:228px;width:380px">Aisha, a non-professional guitar enthusiast<br>will teach beginner guitar for only $5</div>
<svg class="abs pin" style="left:250px;top:314px" viewBox="0 0 20 26" aria-hidden="true"><path d="M10 1C5 1 1 5 1 10c0 7 9 15 9 15s9-8 9-15c0-5-4-9-9-9z" fill="#c9282d"/><circle cx="10" cy="10" r="4" fill="#f2b5b5"/></svg>

<div class="abs callout" style="left:482px;top:384px;width:383px">Mei Ling, an architecture undergraduate<br>will design your home from only 2500$</div>
<div class="abs portrait second" style="left:863px;top:347px" role="img" aria-label="Photo of Mei Ling in glasses holding rolled architectural plans"></div>
<svg class="abs pin" style="left:918px;top:466px" viewBox="0 0 20 26" aria-hidden="true"><path d="M10 1C5 1 1 5 1 10c0 7 9 15 9 15s9-8 9-15c0-5-4-9-9-9z" fill="#c9282d"/><circle cx="10" cy="10" r="4" fill="#f2b5b5"/></svg>

<!-- Services -->
<div class="abs col-divider" style="left:430px"></div>
<div class="abs col-divider" style="left:767px"></div>

<svg class="abs" style="left:128px;top:619px" width="24" height="26" viewBox="0 0 24 26" aria-hidden="true"><circle cx="12" cy="7" r="6" fill="var(--lime)"/><path d="M1 25c0-8 5-11 11-11s11 3 11 11z" fill="var(--lime)"/></svg>
<div class="abs feature-title" style="left:165px;top:623px">Professional Services</div>
<div class="abs feature-rule" style="left:123px;top:666px"></div>
<div class="abs feature-text" style="left:125px;top:678px">On sait depuis longtemps que travailler avec du texte lisible et contenant du sens.</div>
<div class="abs go" style="left:125px;top:729px">GO</div>

<svg class="abs" style="left:463px;top:618px" width="30" height="28" viewBox="0 0 30 28" aria-hidden="true"><rect x="2" y="6" width="20" height="20" fill="none" stroke="var(--lime)" stroke-width="3"/><path d="M10 18l3-7 12-10 4 4-12 10z" fill="var(--lime)"/></svg>
<div class="abs feature-title" style="left:501px;top:623px">Non-Professionals</div>
<div class="abs feature-rule" style="left:460px;top:666px"></div>
<div class="abs feature-text" style="left:462px;top:678px">On sait depuis longtemps que travailler avec du texte lisible et contenant du sens.</div>
<div class="abs go" style="left:462px;top:729px">GO</div>

<svg class="abs" style="left:795px;top:614px" width="34" height="32" viewBox="0 0 34 32" aria-hidden="true"><path d="M2 17l6-3 6 8L30 2l3 2-18 27z" fill="var(--lime)"/></svg>
<div class="abs feature-title" style="left:837px;top:614px">Selling, helping, lending<br>and borrowing</div>
<div class="abs feature-rule" style="left:796px;top:666px"></div>
<div class="abs feature-text" style="left:799px;top:678px">On sait depuis longtemps que travailler avec du texte lisible et contenant du sens.</div>
<div class="abs go" style="left:799px;top:729px">GO</div>

<!-- Lower -->
<section class="abs lower"></section>

<h2 class="abs section-title" style="left:126px;color:var(--navy);font-weight:400">LATEST LISTINGS</h2>
<h2 class="abs section-title" style="left:445px;color:var(--red);font-weight:400;top:808px">LATEST MEMBERS</h2>
<h2 class="abs section-title" style="left:762px;color:var(--green);font-weight:400;top:808px">JOIN US</h2>

<div class="abs listings">
  <div class="abs scroll-track"></div>
  <div class="abs scroll-thumb"></div>
  <svg class="abs" style="left:274px;top:8px" width="18" height="18" viewBox="0 0 18 18" aria-hidden="true"><circle cx="9" cy="9" r="8" fill="#5b8fd0"/><path d="M5 11l4-4 4 4" stroke="#fff" stroke-width="2" fill="none"/></svg>
  <svg class="abs" style="left:274px;top:214px" width="18" height="18" viewBox="0 0 18 18" aria-hidden="true"><circle cx="9" cy="9" r="8" fill="#5b8fd0"/><path d="M5 7l4 4 4-4" stroke="#fff" stroke-width="2" fill="none"/></svg>

  <div class="abs listing-thumb" style="left:13px;top:26px" role="img" aria-label="Member photo of a man"></div>
  <div class="abs listing-title" style="left:74px;top:24px">Composition et la mise en.</div>
  <div class="abs listing-rule" style="left:74px;top:44px"></div>
  <div class="abs listing-text" style="left:75px;top:50px">Lorem Ipsum est simplement du faux texte employé dans la sition et la misen page avant...</div>
  <div class="abs listing-meta" style="left:75px;top:95px">5 comment</div>
  <svg class="abs" style="left:140px;top:96px" width="10" height="10" viewBox="0 0 10 10" aria-hidden="true"><path d="M4 0h2v4h4v2H6v4H4V6H0V4h4z" fill="var(--lime)"/></svg>
  <svg class="abs" style="left:167px;top:94px" width="30" height="14" viewBox="0 0 30 14" aria-hidden="true"><path d="M1 6h3v7H1zM5 6l3-5c2 0 2 2 1 4h4l-1 8H5z" fill="#999"/><path d="M17 1h3v7h-3zM21 8l3 5c2 0 2-2 1-4h4l-1-8h-7z" fill="#999"/></svg>
  <div class="abs listing-meta" style="left:212px;top:95px">4 July 2012</div>

  <div class="abs listing-thumb light" style="left:13px;top:131px" role="img" aria-label="Member photo of a woman"></div>
  <div class="abs listing-title" style="left:74px;top:129px">Composition et la mise en.</div>
  <div class="abs listing-rule" style="left:74px;top:149px"></div>
  <div class="abs listing-text" style="left:75px;top:155px">Lorem Ipsum est simplement du faux texte employé dans la sition et la misen page avant...</div>
  <div class="abs listing-meta" style="left:75px;top:200px">5 comment</div>
  <svg class="abs" style="left:140px;top:201px" width="10" height="10" viewBox="0 0 10 10" aria-hidden="true"><path d="M4 0h2v4h4v2H6v4H4V6H0V4h4z" fill="var(--lime)"/></svg>
  <svg class="abs" style="left:167px;top:199px" width="30" height="14" viewBox="0 0 30 14" aria-hidden="true"><path d="M1 6h3v7H1zM5 6l3-5c2 0 2 2 1 4h4l-1 8H5z" fill="#999"/><path d="M17 1h3v7h-3zM21 8l3 5c2 0 2-2 1-4h4l-1-8h-7z" fill="#999"/></svg>
  <div class="abs listing-meta" style="left:212px;top:200px">4 July 2012</div>
</div>

<div class="abs member" style="left:447px;top:846px" role="img" aria-label="Member photo"></div>
<div class="abs member" style="left:521px;top:846px;background:linear-gradient(160deg,#d8b497,#a07a60)" role="img" aria-label="Member photo"></div>
<div class="abs member" style="left:595px;top:846px;background:linear-gradient(160deg,#a8705a,#5a3a30)" role="img" aria-label="Member photo"></div>
<div class="abs member" style="left:669px;top:846px;background:linear-gradient(160deg,#e6e6e6,#8a8f96)" role="img" aria-label="Member photo"></div>
<div class="abs member" style="left:447px;top:921px;background:linear-gradient(160deg,#dfe4e8,#9ba6b0)" role="img" aria-label="Member photo"></div>
<div class="abs member" style="left:521px;top:921px;background:linear-gradient(160deg,#e27a3a,#b9522a)" role="img" aria-label="Member photo"></div>
<div class="abs member" style="left:595px;top:921px;background:linear-gradient(160deg,#4a4a52,#1e1e24)" role="img" aria-label="Member photo"></div>
<div class="abs member" style="left:669px;top:921px;background:linear-gradient(160deg,#cfd3d6,#3a3c40)" role="img" aria-label="Member photo"></div>

<div class="abs promo">LOREM IPSUM DOLOR SIT AMET,<br>CONS ECTETUR ADIPSCING ELIT</div>
<div class="abs show-all">SHOW ALL.</div>

<div class="abs signup">
  <div class="abs signup-title">SIGN UP</div>
  <div class="abs signup-rule"></div>
  <div class="abs signup-field" style="top:62px">Username</div>
  <div class="abs signup-field" style="top:101px">Password</div>
  <div class="abs btn-next">Next</div>
  <div class="abs agree">I Agree</div>
  <div class="abs agree-box"></div>
  <div class="abs signup-link" style="top:202px">FORGOT PASSWORD ?</div>
  <div class="abs signup-link" style="top:222px">RESEND ACTIVATION CODE</div>
</div>

<footer class="abs footer"></footer>
<div class="abs footer-text" style="left:126px">copyright©2013. All Rights Reserved</div>
<div class="abs footer-text" style="left:752px">Spread the nestlinker</div>
<div class="abs share-btn" style="left:918px;width:40px">Like</div>
<div class="abs share-btn" style="left:969px;width:35px">+1</div>
<div class="abs share-btn" style="left:1012px;width:46px">Share</div>

</body>
</html>
```